M Zyvantics Buisness Cards

I need a technology focused clean business card for my employees. I have attached out logo to include in the mocks. We're a modern tech consulting firm that drives to interface humanity with technology in a truly cohesive fashion.

```html
<!DOCTYPE html>
<html lang="en">
<head>
<meta charset="utf-8">
<title>M Zyvantics Business Cards</title>
<link rel="stylesheet" href="https://fonts.googleapis.com/css2?family=Exo+2:wght@500;600&display=swap">
<style>
  :root {
    --page-bg: #e7e4df;
    --card-white: #f4f4f4;
    --brand-blue: #1f76c2;
    --brand-blue-light: #3a88cf;
    --brand-grey: #7d7f83;
    --ink: #3b3c3e;
    --white: #ffffff;
  }
  html, body {
    margin: 0;
    width: 900px;
    height: 1200px;
    overflow: hidden;
    background: var(--page-bg);
    font-family: "Exo 2", sans-serif;
  }
  .canvas {
    position: relative;
    width: 900px;
    height: 1200px;
  }
  .card {
    position: absolute;
    left: 88px;
    width: 734px;
    height: 430px;
    border-radius: 22px;
    overflow: hidden;
    box-shadow: 0 6px 14px rgba(0, 0, 0, 0.25);
  }
  .card-front {
    top: 125px;
    background: linear-gradient(135deg, #ffffff 0%, var(--card-white) 60%, #e9e9e9 100%);
  }
  .card-back {
    top: 640px;
    background: var(--brand-blue);
  }
  .front-feature {
    position: absolute;
    left: 442px;
    top: 0;
    right: 0;
    bottom: 0;
    background:
      radial-gradient(circle at 100% 50%, rgba(31, 118, 194, 0.22) 0%, rgba(31, 118, 194, 0.10) 45%, rgba(125, 127, 131, 0.10) 70%, rgba(255, 255, 255, 0) 100%);
  }
  .brand-name {
    position: absolute;
    left: 50px;
    top: 60px;
    display: flex;
    align-items: center;
    gap: 14px;
    font-weight: 600;
    font-size: 44px;
    line-height: 1;
    color: var(--brand-blue);
    letter-spacing: 0.5px;
  }
  .brand-dot {
    width: 22px;
    height: 22px;
    border-radius: 50%;
    background: var(--brand-blue);
    flex: none;
  }
  .person-name {
    position: absolute;
    left: 50px;
    top: 176px;
    margin: 0;
    font-weight: 600;
    font-size: 30px;
    line-height: 1;
    color: var(--ink);
    letter-spacing: 0.6px;
  }
  .person-title {
    position: absolute;
    left: 50px;
    top: 213px;
    margin: 0;
    font-weight: 500;
    font-size: 19px;
    line-height: 1;
    color: var(--brand-blue);
    letter-spacing: 0.3px;
  }
  .contact-list {
    position: absolute;
    left: 50px;
    top: 259px;
    margin: 0;
    padding: 0;
    list-style: none;
  }
  .contact-list li {
    display: flex;
    align-items: center;
    gap: 11px;
    height: 23.7px;
    font-size: 16.5px;
    font-weight: 500;
    color: var(--ink);
    letter-spacing: 0.5px;
  }
  .contact-icon {
    width: 14px;
    height: 14px;
    fill: var(--brand-blue);
    flex: none;
  }
  .address {
    position: absolute;
    left: 50px;
    top: 378px;
    margin: 0;
    font-size: 16.5px;
    font-weight: 500;
    line-height: 1;
    color: var(--ink);
    letter-spacing: 0.7px;
  }
  .back-texture {
    position: absolute;
    inset: 0;
    background:
      radial-gradient(circle at 30% 35%, rgba(255, 255, 255, 0.10) 0%, rgba(255, 255, 255, 0) 55%),
      linear-gradient(180deg, var(--brand-blue-light) 0%, var(--brand-blue) 55%, #1d70ba 100%);
  }
  .back-brand {
    position: absolute;
    right: 56px;
    top: 296px;
    display: flex;
    align-items: center;
    gap: 10px;
    font-weight: 600;
    font-size: 30px;
    line-height: 1;
    color: var(--white);
  }
  .back-brand .brand-dot {
    width: 14px;
    height: 14px;
    background: var(--white);
  }
</style>
</head>
<body>
<main class="canvas">
  <section class="card card-front" aria-label="Business card front">
    <div class="front-feature" role="img" aria-label="Large cropped brand emblem in grey and blue"></div>
    <div class="brand-name"><span class="brand-dot"></span>M Zyvantics</div>
    <h1 class="person-name">Daniel Reyes</h1>
    <p class="person-title">Managing Director</p>
    <ul class="contact-list">
      <li>
        <svg class="contact-icon" viewBox="0 0 16 16" aria-hidden="true"><path d="M3.6 1.2l2.3 2.7-1.4 1.8c.9 2 2.6 3.7 4.6 4.6l1.8-1.4 2.7 2.3-1.3 2.2C7.1 13.6 2.4 8.9 1.4 3z"/></svg>
        555.310.4821
      </li>
      <li>
        <svg class="contact-icon" viewBox="0 0 16 16" aria-hidden="true"><path d="M4 1h8v4H4zM1 6h14v6h-3v-2H4v2H1zM5 11h6v4H5z"/></svg>
        555.310.4822
      </li>
      <li>
        <svg class="contact-icon" viewBox="0 0 16 16" aria-hidden="true"><path d="M1 3h14v10H1zm1.6 1.4v.4L8 8.6l5.4-3.8v-.4zM2.6 6.4v5.2h10.8V6.4L8 10.2z"/></svg>
        daniel@mzyvantics.com
      </li>
      <li>
        <svg class="contact-icon" viewBox="0 0 16 16" aria-hidden="true"><path d="M8 1a7 7 0 100 14A7 7 0 008 1zm0 1.4c.7 0 1.6 1.4 1.9 3.6H6.1C6.4 3.8 7.3 2.4 8 2.4zM5 6H2.7a5.6 5.6 0 012.9-3.1C5.3 3.7 5.1 4.8 5 6zm6 0c-.1-1.2-.3-2.3-.6-3.1A5.6 5.6 0 0113.3 6zM2.5 7.4H5v1.2H2.5zm3.6 0h3.8v1.2H6.1zm4.9 0h2.5v1.2H11zM2.7 10H5c.1 1.2.3 2.3.6 3.1A5.6 5.6 0 012.7 10zm3.4 0h3.8c-.3 2.2-1.2 3.6-1.9 3.6s-1.6-1.4-1.9-3.6zm4.9 0h2.3a5.6 5.6 0 01-2.9 3.1c.3-.8.5-1.9.6-3.1z"/></svg>
        www.mzyvantics.com
      </li>
    </ul>
    <p class="address">4180 Harbor Lane, Suite 210, Dayton, OH 45402</p>
  </section>

  <section class="card card-back" aria-label="Business card back">
    <div class="back-texture" role="img" aria-label="Faint repeating brand emblem pattern on blue"></div>
    <div class="back-brand"><span class="brand-dot"></span>M Zyvantics</div>
  </section>
</main>
</body>
</html>
```